KESTREL Communications Business Card- Belsa

Kestrel Integrated Communications is Corporate communications agency with more than 20 years of experience. We become part of the manegement team of our clients in other to improve their outcomes and grow the possitioning of their brand.
We are in Puerto Rico, latin caribbean island
Name: Maribelsa (Belsa) Ocampo
787-555-0148
bocampo@kestrelwing.example

Target Market(s)

finance and pharmaceutical companies

Industry/Entity Type

Business

Contact Information for Business Card

modern, edgy colorful and playfull like our logo

Requirements
Must have
• company logo
• name
• tel
• email

```html
<!DOCTYPE html>
<html lang="en">
<head>
<meta charset="utf-8">
<title>Kestrel Integrated Communications – Business Card – Belsa</title>
<link rel="stylesheet" href="https://fonts.googleapis.com/css2?family=Open+Sans:wght@400;600;700&display=swap">
<style>
  :root {
    --backdrop: #2b2b2b;
    --card-black: #050505;
    --white: #ffffff;
    --orange: #f15a24;
  }
  html, body {
    margin: 0;
    padding: 0;
    width: 1200px;
    height: 900px;
    overflow: hidden;
    background: var(--backdrop);
    font-family: "Open Sans", Arial, sans-serif;
  }
  .canvas {
    position: relative;
    width: 1200px;
    height: 900px;
  }
  .card {
    position: absolute;
    left: 250px;
    width: 700px;
    height: 400px;
    background: var(--card-black);
    overflow: hidden;
    box-shadow: 0 10px 24px rgba(0,0,0,0.45);
  }
  .card--front { top: 30px; }
  .card--back  { top: 470px; }

  .wordmark {
    display: flex;
    align-items: center;
    gap: 14px;
    color: var(--white);
    font-weight: 700;
  }
  .wordmark__dot {
    width: 22px;
    height: 22px;
    border-radius: 50%;
    background: var(--orange);
    flex: none;
  }
  .wordmark__text { display: flex; flex-direction: column; line-height: 1; }
  .wordmark__name { letter-spacing: 0.04em; }
  .wordmark__tagline { letter-spacing: 0.14em; margin-top: 8px; }

  .card--front .wordmark {
    position: absolute;
    left: 50%;
    top: 50%;
    transform: translate(-50%, -50%);
  }
  .card--front .wordmark__name { font-size: 62px; }
  .card--front .wordmark__tagline { font-size: 13px; }

  .card--back .wordmark {
    position: absolute;
    left: 48px;
    top: 160px;
  }
  .card--back .wordmark__name { font-size: 38px; }
  .card--back .wordmark__tagline { font-size: 8.5px; }

  .contact {
    position: absolute;
    left: 360px;
    top: 120px;
    color: var(--white);
  }
  .contact__name {
    margin: 0 0 14px;
    font-size: 21px;
    font-weight: 700;
    letter-spacing: 0.02em;
    text-transform: uppercase;
  }
  .contact__line {
    display: flex;
    align-items: center;
    gap: 8px;
    margin: 4px 0 0 4px;
    font-size: 14px;
    color: var(--orange);
  }
  .contact__icon { width: 11px; height: 11px; flex: none; }

  .footer-rule {
    position: absolute;
    left: 0;
    right: 0;
    bottom: 50px;
    height: 3px;
    background: var(--white);
  }
  .footer-band {
    position: absolute;
    left: 0;
    right: 0;
    bottom: 0;
    height: 42px;
    background: var(--orange);
  }
</style>
</head>
<body>
<main class="canvas">
  <section class="card card--front" aria-label="Card front">
    <div class="wordmark">
      <span class="wordmark__dot"></span>
      <span class="wordmark__text">
        <span class="wordmark__name">KESTREL</span>
        <span class="wordmark__tagline">INTEGRATED COMMUNICATIONS</span>
      </span>
    </div>
  </section>

  <section class="card card--back" aria-label="Card back">
    <div class="wordmark">
      <span class="wordmark__dot"></span>
      <span class="wordmark__text">
        <span class="wordmark__name">KESTREL</span>
        <span class="wordmark__tagline">INTEGRATED COMMUNICATIONS</span>
      </span>
    </div>

    <div class="contact">
      <h1 class="contact__name">Maribelsa (Belsa) Ocampo</h1>
      <p class="contact__line">
        <svg class="contact__icon" viewBox="0 0 24 24" aria-hidden="true"><path fill="#ffffff" d="M6.6 10.8a15.1 15.1 0 0 0 6.6 6.6l2.2-2.2a1 1 0 0 1 1-.25 11.4 11.4 0 0 0 3.6.57 1 1 0 0 1 1 1V20a1 1 0 0 1-1 1A17 17 0 0 1 3 4a1 1 0 0 1 1-1h3.5a1 1 0 0 1 1 1c0 1.25.2 2.45.57 3.57a1 1 0 0 1-.25 1z"/></svg>
        787-555-0148
      </p>
      <p class="contact__line">
        <svg class="contact__icon" viewBox="0 0 24 24" aria-hidden="true"><rect x="2" y="5" width="20" height="14" fill="none" stroke="#ffffff" stroke-width="2"/><path d="M2 6l10 7 10-7" fill="none" stroke="#ffffff" stroke-width="2"/></svg>
        bocampo@kestrelwing.example
      </p>
    </div>

    <div class="footer-rule"></div>
    <div class="footer-band"></div>
  </section>
</main>
</body>
</html>
```